依頼詳細
サイト構成・基本的な要件については
https://zuvexo.example/boards/R7pQ2mXa9TkWvHcY/B58F3
をご参照ください。

ただ、レイアウトについては、各コンテンツへの導線が確保されていれば、
上記レイアウト案を必ず守る必要はございません。
また、当方jqueryを使用したコーディングも可能です。

提出の写真素材は
https://qlbox.example/T9wRkA
上記のものをご利用いただければ幸いです。

現在、素材があまり集まっていないため、
http://fotmira.example/
などから、10000円程度までならこちらにて購入可能です。
カンプデータにて作成頂き、納品時に当方にて購入したデータに差し替えていただければと存じます。

https://images.velonta.example/jp/
についても定期購入しておりますので、
5点ほどでしたら取得可能です。

また、既存サイト
https://www.harimoku.example/
に使用されている画像は自由にご利用ください。

【参考サイト】
https://www.tzr-worldwide.example/jp/
https://morifusa.example/
https://hotarubako.example/
https://www.calmfield.example/
https://www.yosetabi.example/

写真を大きく見せ、
高級感があり、訴求力の高いデザインを希望します。

色合いは、現在のサイト同様、
モノトーンをベースに、差し色を使用する場合は1色程度、
シックで高級感のある色合いを希望いたします。
サイトURL
ページ数
1ページ
希望イメージ
シンプル 複雑
単色 カラフル
暗い 明るい
日常 高級
遊び心 厳粛
未来的 伝統的
女性的 男性的
希望する色
グレー系
納品ファイル
• 高解像度JPG (.jpg)
• フォトショップ形式 (.psd)
補足説明
提出の写真素材は
https://qlbox.example/T9wRkA
上記アップロードしたものをご利用いただければ幸いです。

現在、素材があまり集まっていないため、
http://fotmira.example/
についても定期購入しておりますので、
5点ほどでしたら取得可能です。

納品データはPSDのほか
XDの提出でも問題ございません。

制作に関してご不明な点がございましたら
お気軽にお申し付けください。

何卒宜しくお願い致します。

```html
<!DOCTYPE html>
<html lang="ja">
<head>
<meta charset="utf-8">
<title>ハリモク | Beauty and Function</title>
<link href="https://fonts.googleapis.com/css2?family=Playfair+Display:wght@400;500&family=Cormorant+Garamond:wght@300;400;500&family=Great+Vibes&family=Noto+Serif+JP:wght@300;400;500&display=swap" rel="stylesheet">
<style>
:root{
  --bg:#0d0d0d;
  --ink:#e9e9e9;
  --muted:#8a8a8a;
  --dim:#4a4a4a;
  --ghost:#2a2a2a;
  --line:#2b2b2b;
  --footer:#262626;
  --serif-en:"Cormorant Garamond", serif;
  --display:"Playfair Display", serif;
  --jp:"Noto Serif JP", serif;
}
*{margin:0;padding:0;box-sizing:border-box}
html,body{width:1200px;height:4104px;overflow:hidden;background:var(--bg);color:var(--ink);font-family:var(--jp)}
.page{position:relative;width:1200px;height:4104px}
.abs{position:absolute}
.photo{position:absolute}

/* header */
.brand{left:56px;top:22px;font-family:var(--serif-en);font-size:22px;letter-spacing:4px;font-weight:500;display:flex;align-items:center;gap:8px}
.brand i{display:block;width:8px;height:8px;background:var(--ink)}
.gnav{left:368px;top:26px;display:flex;gap:44px;font-family:var(--serif-en);font-size:17px;color:#cfcfcf}

/* hero */
.hero-word{font-family:var(--display);color:var(--ghost);line-height:1;white-space:nowrap}
.hero-beauty{left:300px;top:-70px;font-size:260px}
.hero-and{left:150px;top:250px;font-family:"Great Vibes",cursive;font-size:150px;color:#333}
.hero-function{left:-10px;top:400px;font-size:270px}
.hero-photo{left:420px;top:80px;width:360px;height:520px;background:linear-gradient(160deg,#f4f1ea 0%,#cfc6b8 45%,#6a5a48 100%)}
.hero-lead{left:820px;top:262px}
.hero-lead h2{font-size:22px;font-weight:400;letter-spacing:3px}
.hero-lead .en{font-family:var(--serif-en);font-size:14px;color:var(--muted);margin-top:8px;letter-spacing:1px}
.hero-lead p{font-size:14px;line-height:2.1;color:#bdbdbd;margin-top:44px;width:320px}

/* about */
.vlabel{writing-mode:vertical-rl;font-family:var(--serif-en);font-size:15px;letter-spacing:4px;color:var(--muted)}
.about-label{left:90px;top:860px}
.about-head{left:240px;top:850px;font-size:19px;line-height:1.9;letter-spacing:2px;font-weight:400}
.about-body{left:240px;top:960px;width:420px;font-size:13px;line-height:2.15;color:#b3b3b3}
.about-body p+p{margin-top:24px}

/* category */
.sec-label{font-family:var(--serif-en);font-size:20px;letter-spacing:1px}
.cat-label{left:96px;top:1500px}
.cat-list{left:96px;top:1560px;width:1008px;list-style:none}
.cat-list li{height:86px;border-bottom:1px solid var(--line);display:flex;align-items:center;gap:18px}
.cat-list .en{font-family:var(--serif-en);font-size:50px;color:var(--dim);font-weight:400}
.cat-list .jp{font-size:11px;color:var(--dim);letter-spacing:1px}
.cat-list li.on .en,.cat-list li.on .jp{color:var(--ink)}
.cat-photo{left:752px;top:1680px;width:316px;height:180px;background:linear-gradient(120deg,#e8e6e2,#a9a39b 60%,#56514a)}

/* works */
.works-label{left:96px;top:2396px}
.works-arrows{left:1036px;top:2400px;display:flex;gap:22px}
.work{top:2460px;height:280px}
.w1{left:96px;width:372px;background:linear-gradient(140deg,#3a3026,#c6b79f 55%,#eee7da)}
.w2{left:488px;width:376px;background:linear-gradient(150deg,#f2f2f2,#c9c7c4 60%,#7b3b30)}
.w3{left:880px;width:320px;background:linear-gradient(170deg,#1b1b1b 0 35%,#d9d9d9 55%,#8c8c8c)}
.cap{top:2758px;font-size:12px;color:#bdbdbd}

/* news */
.news-photo{left:0;top:2920px;width:300px;height:160px;background:linear-gradient(90deg,#3c3c3c,#1a1a1a)}
.news-label{left:284px;top:2948px}
.news-list{left:420px;top:2960px;width:700px;list-style:none}
.news-list li{height:72px;border-bottom:1px solid var(--line);display:flex;align-items:center;font-size:12px;color:#bdbdbd}
.news-list time{width:160px;font-family:var(--serif-en);font-size:14px;color:var(--muted)}
.view-all{left:990px;top:3422px;font-family:var(--serif-en);font-size:15px;display:flex;align-items:center;gap:10px}

/* contact */
.contact{left:0;top:3470px;width:1200px;text-align:center}
.contact h2{font-family:var(--display);font-weight:400;font-size:76px;letter-spacing:2px}
.contact .rule{width:300px;height:1px;background:var(--ink);margin:4px auto 0}
.contact p{font-size:12px;color:#bdbdbd;margin-top:22px;letter-spacing:1px}

/* footer */
.footer{left:188px;top:3760px;width:1012px;height:344px;background:var(--footer)}
.f-brand{left:84px;top:50px;font-family:var(--serif-en);font-size:18px;letter-spacing:3px;display:flex;align-items:center;gap:8px}
.f-brand i{width:7px;height:7px;background:var(--ink);display:block}
.f-tel{left:84px;top:112px;font-family:var(--serif-en);font-size:40px;letter-spacing:1px}
.f-hours{left:84px;top:168px;font-size:11px;color:var(--muted)}
.f-addr{left:84px;top:210px;font-size:11px;line-height:1.9;color:var(--muted)}
.f-nav{left:520px;top:212px;display:flex;gap:48px;font-family:var(--serif-en);font-size:15px;color:#cfcfcf}
.f-copy{left:84px;top:300px;font-size:10px;color:#6d6d6d;font-family:var(--serif-en);letter-spacing:1px}
</style>
</head>
<body>
<div class="page">

  <header>
    <div class="abs brand"><i></i>HARIMOKU</div>
    <nav class="abs gnav"><span>Top</span><span>Works</span><span>Flow</span><span>Workflow</span><span>Company</span><span>Contact</span><span>Recruit</span></nav>
  </header>

  <section class="hero">
    <div class="abs hero-word hero-beauty">Beauty</div>
    <div class="abs hero-word hero-and">and</div>
    <div class="abs hero-word hero-function">Function</div>
    <div class="photo hero-photo" role="img" aria-label="吹き抜けと階段のある明るいリビングの写真"></div>
    <div class="abs hero-lead">
      <h2>快適居住空間の演出</h2>
      <div class="en">We create comfortable living space.</div>
      <p>ひとりひとりに合った住まいをトータルに。<br>ハリモクは、より良い住空間を目指して、<br>機能性と美しさを兼ね備えた空間をご提案します。</p>
    </div>
  </section>

  <section class="about">
    <div class="abs vlabel about-label">About</div>
    <h2 class="abs about-head">ハリモクは手仕事と品質にこだわり、<br>一人ひとりに合った住空間をご提案しています</h2>
    <div class="abs about-body">
      <p>1998年、東京都内のマンション・住宅・店舗・オフィスなどのリフォームを中心に創業。以来、施工実績を重ね、デザインと機能の両立を大切にしてまいりました。</p>
      <p>お客様の暮らしに寄り添い、素材選びから仕上げまで丁寧に向き合うことが、私たちの変わらない姿勢です。</p>
      <p>細部まで妥協しない施工で、長く愛される住まいづくりを心がけ、一つひとつの現場に誠実に取り組んでいます。</p>
    </div>
    <div class="photo" style="left:692px;top:832px;width:160px;height:336px;background:linear-gradient(160deg,#f1ede6,#b89a78 60%,#a3372c)" role="img" aria-label="赤い絵画が飾られたダイニングの写真"></div>
    <div class="photo" style="left:936px;top:832px;width:136px;height:200px;background:linear-gradient(170deg,#f3f3f1,#c8c2b8)" role="img" aria-label="白い廊下の写真"></div>
    <div class="photo" style="left:936px;top:1072px;width:192px;height:288px;background:linear-gradient(170deg,#f6f4f0,#cdbfa9 70%,#8a7659)" role="img" aria-label="玄関ホールの写真"></div>
  </section>

  <section class="category">
    <h2 class="abs sec-label cat-label">Reform Category</h2>
    <ul class="abs cat-list">
      <li><span class="en">Design Reform</span><span class="jp">デザインリフォーム</span></li>
      <li><span class="en">Kitchen Reform</span><span class="jp">キッチンリフォーム</span></li>
      <li class="on"><span class="en">Washbasin/Bathroom</span><span class="jp">洗面・浴室リフォーム</span></li>
      <li><span class="en">Kids Room</span><span class="jp">子供部屋</span></li>
      <li><span class="en">Entrance</span><span class="jp">玄関リフォーム</span></li>
      <li><span class="en">Exterior</span><span class="jp">外装リフォーム</span></li>
      <li><span class="en">Shop/Office</span><span class="jp">店舗・オフィス</span></li>
      <li><span class="en">Partial Reform</span><span class="jp">部分リフォーム</span></li>
    </ul>
    <div class="photo cat-photo" role="img" aria-label="洗面台と浴室の写真"></div>
  </section>

  <section class="works">
    <h2 class="abs sec-label works-label">Recent works</h2>
    <div class="abs works-arrows">
      <svg width="20" height="12" viewBox="0 0 20 12"><path d="M20 6H2M7 1 2 6l5 5" stroke="#e9e9e9" fill="none"/></svg>
      <svg width="20" height="12" viewBox="0 0 20 12"><path d="M0 6h18M13 1l5 5-5 5" stroke="#e9e9e9" fill="none"/></svg>
    </div>
    <div class="photo work w1" role="img" aria-label="ソファのある暖色照明のリビングの写真"></div>
    <div class="photo work w2" role="img" aria-label="赤いソファのある白いリビングの写真"></div>
    <div class="photo work w3" role="img" aria-label="黒い天井のモダンなキッチンの写真"></div>
    <div class="abs cap" style="left:96px">S邸　デザインリフォーム</div>
    <div class="abs cap" style="left:488px">K邸　デザインリフォーム</div>
    <div class="abs cap" style="left:880px">M邸キッチン　デザインリフォーム</div>
  </section>

  <section class="news">
    <div class="photo news-photo" role="img" aria-label="暗いインテリアの写真"></div>
    <h2 class="abs sec-label news-label">News</h2>
    <ul class="abs news-list">
      <li><time>2019.03.12</time>施工事例を追加しました</li>
      <li><time>2019.02.25</time>休業日のお知らせ</li>
      <li><time>2019.02.08</time>ホームページをリニューアルしました</li>
      <li><time>2019.01.21</time>春のリフォーム相談会を開催します（3月開催予定）</li>
      <li><time>2019.01.07</time>施工事例を追加しました</li>
    </ul>
    <div class="abs view-all">view all
      <svg width="22" height="10" viewBox="0 0 22 10"><path d="M0 5h20M16 1l4 4-4 4" stroke="#e9e9e9" fill="none"/></svg>
    </div>
  </section>

  <section class="abs contact">
    <h2>Contact</h2>
    <div class="rule"></div>
    <p>お見積りのご相談やご質問はお気軽にお問い合わせください。</p>
  </section>

  <footer class="abs footer">
    <div class="abs f-brand"><i></i>HARIMOKU</div>
    <div class="abs f-tel">03-5550-0142</div>
    <div class="abs f-hours">受付時間 9:00〜18:00（日・祝休）</div>
    <div class="abs f-addr">〒100-0000 東京都架空区見本町1-2-3<br>サンプルビル 4F</div>
    <nav class="abs f-nav"><span>Top</span><span>Works</span><span>Workflow</span><span>Company</span><span>Recruit</span></nav>
    <div class="abs f-copy">Copyright © HARIMOKU All Rights Reserved.</div>
  </footer>

</div>
</body>
</html>
```